7 Vex Label

Design a label for 7 Vex styling gels. The logo is attached. The color is C=100, M=100, Y=0, K=0. The 16 oz. jar is also attached.

Updates

Attention all designers,

The old logo has been deleted.  I have uploaded a new logo for this project.  Can you please update your design with the NEW LOGO?
thank you,
Rob

Target Market(s)

Multicultural

Requirements
Must have
• you must used the logo attached.

text to be included on the jar:

Used by Professionals
Maximum Hold
Alcohol Free
NO FLAKING

16 oz.

As far as label size, use the jar photo, and fit the design on it.

```html
<!DOCTYPE html>
<html lang="en">
<head>
<meta charset="utf-8">
<title>7 Vex Label</title>
<link href="https://fonts.googleapis.com/css2?family=Libre+Baskerville:wght@700&display=swap" rel="stylesheet">
<style>
  :root {
    --brand-blue: #13289a;
    --paper: #ffffff;
    --shadow: rgba(0, 0, 0, 0.35);
  }
  html, body {
    margin: 0;
    padding: 0;
    width: 1200px;
    height: 1000px;
    overflow: hidden;
    background: var(--paper);
  }
  .canvas {
    position: relative;
    width: 1200px;
    height: 1000px;
    font-family: "Libre Baskerville", "Times New Roman", serif;
    font-weight: 700;
  }
  .label {
    position: absolute;
    left: 175px;
    top: 115px;
    width: 665px;
    height: 247px;
    background: var(--brand-blue);
    box-shadow: 0 8px 8px var(--shadow);
    color: var(--paper);
    overflow: hidden;
  }
  .label__claim {
    position: absolute;
    margin: 0;
    font-size: 15px;
    white-space: nowrap;
  }
  .label__claim--alcohol { left: 22px; top: 40px; }
  .label__claim--pros { right: 85px; top: 16px; }
  .label__claim--flaking { right: 85px; top: 49px; }
  .label__claim--hold { right: 85px; top: 216px; }
  .label__size {
    position: absolute;
    left: 70px;
    top: 212px;
    margin: 0;
    font-size: 23px;
  }
  .label__emblem {
    position: absolute;
    left: 148px;
    top: -12px;
    width: 264px;
    height: 264px;
    border-radius: 50%;
    background: var(--paper);
    display: flex;
    align-items: center;
    justify-content: center;
  }
  .label__emblem-name {
    color: var(--brand-blue);
    font-size: 64px;
    margin: 0;
  }
  .label__brand-vertical {
    position: absolute;
    left: 598px;
    top: 0;
    width: 60px;
    height: 247px;
    display: flex;
    align-items: center;
    justify-content: center;
  }
  .label__brand-vertical span {
    transform: rotate(-90deg);
    font-size: 40px;
    white-space: nowrap;
    letter-spacing: 4px;
  }
  .brand-mark {
    position: absolute;
    left: 858px;
    top: 212px;
    width: 175px;
    display: flex;
    align-items: center;
    gap: 10px;
  }
  .brand-mark__dot {
    width: 70px;
    height: 70px;
    border-radius: 50%;
    background: var(--brand-blue);
    flex: none;
  }
  .brand-mark__name {
    color: var(--brand-blue);
    font-size: 40px;
    margin: 0;
    white-space: nowrap;
  }
</style>
</head>
<body>
<main class="canvas">
  <section class="label" aria-label="7 Vex styling gel label">
    <p class="label__claim label__claim--alcohol">Alcohol Free</p>
    <div class="label__emblem">
      <p class="label__emblem-name">7 Vex</p>
    </div>
    <p class="label__claim label__claim--pros">Used by Professionals</p>
    <p class="label__claim label__claim--flaking">NO FLAKING</p>
    <p class="label__size">16 oz.</p>
    <p class="label__claim label__claim--hold">Maximum Hold</p>
    <div class="label__brand-vertical"><span>7 Vex</span></div>
  </section>

  <div class="brand-mark">
    <span class="brand-mark__dot"></span>
    <p class="brand-mark__name">7 Vex</p>
  </div>
</main>
</body>
</html>
```